Professional Business Cards

We need a nice looking, profession and modern business card for our new company. Our logo is attatched

Target Market(s)

Young Professionals

Industry/Entity Type

Financial

Contact Information for Business Card

FRONT

Morvane Tally Pty Ltd
Level 22, Halden Court, 48 Wirrapool St
Sydney NSW 2000
ABN : 57 304 918 226

Derek Wallis - Chief Operations Officer
P : 02 7153 2819
M: 0418 395 207
derek@morvanetally,com

BACK

- Cryptocurrency Exchange Services
- Cryptocurrency Mining Operations
- Cryptocurrency Investment Fund Offering

Font styles to use
Sans Serif

Colors
0255a3
9d9d9d

```html
<!DOCTYPE html>
<html lang="en">
<head>
<meta charset="utf-8">
<title>Morvane Tally – Business Card</title>
<link rel="stylesheet" href="https://fonts.googleapis.com/css2?family=Fira+Sans+Condensed:ital,wght@1,500;1,600&family=Open+Sans:ital,wght@0,700;1,400&display=swap">
<style>
  :root {
    --brand-blue: #0455a3;
    --brand-grey: #757575;
    --text-grey: #6a6a6a;
    --stage: #c6c6c6;
    --card: #ffffff;
    --label: #000000;
  }
  * { margin: 0; padding: 0; box-sizing: border-box; }
  html, body { width: 1200px; height: 1195px; overflow: hidden; }
  body { background: var(--stage); position: relative; font-family: "Open Sans", Arial, sans-serif; }

  .card { position: absolute; background: var(--card); overflow: hidden; }
  .card--front { left: 181px; top: 12px; width: 834px; height: 509px; }
  .card--back  { left: 182px; top: 617px; width: 836px; height: 509px; }
  .card__stripes { position: absolute; inset: 0; width: 100%; height: 100%; }
  .stripe--blue { fill: var(--brand-blue); }
  .stripe--grey { fill: var(--brand-grey); }

  .company-address {
    position: absolute; left: 17px; top: 16px;
    font-style: italic; font-size: 21px; line-height: 29.3px; color: var(--text-grey);
  }

  .brand {
    position: absolute; left: 50%; top: 255px; transform: translate(-50%, -50%);
    display: flex; align-items: center; gap: 18px; white-space: nowrap;
  }
  .brand__mark { width: 30px; height: 30px; background: var(--brand-blue); }
  .brand__name {
    font-weight: 700; font-size: 44px; color: var(--brand-blue); letter-spacing: 0.5px;
  }

  .contact {
    position: absolute; right: 20px; top: 383px; text-align: right;
    font-style: italic; font-size: 21px; line-height: 29.5px; color: var(--brand-blue);
  }

  .service {
    position: absolute; left: 50%; transform: translate(-50%, -50%); white-space: nowrap;
    font-family: "Fira Sans Condensed", "Arial Narrow", sans-serif;
    font-style: italic; font-weight: 500; font-size: 43px; color: var(--brand-grey);
  }
  .service--exchange { top: 72px; }
  .service--mining { top: 253px; }
  .service--fund { top: 434px; }

  .side-label {
    position: absolute; transform: translate(-50%, -50%);
    font-family: "Fira Sans Condensed", "Arial Narrow", sans-serif;
    font-style: italic; font-weight: 600; font-size: 50px; color: var(--label);
  }
  .side-label--front { left: 608px; top: 563px; }
  .side-label--back { left: 613px; top: 1156px; }
</style>
</head>
<body>

<section class="card card--front">
  <svg class="card__stripes" viewBox="0 0 1024 625" preserveAspectRatio="none" aria-hidden="true">
    <polygon class="stripe--blue" points="0,185 745,171 1024,0 1024,4 752,189 0,189"/>
    <polygon class="stripe--grey" points="0,625 278,442 1024,447 1024,450 281,458 5,625"/>
  </svg>

  <address class="company-address">
    Morvane Tally Pty Ltd<br>
    Level 22, Halden Court, 48 Wirrapool St<br>
    Sydney NSW 2000<br>
    ABN : 57 304 918 226
  </address>

  <div class="brand">
    <span class="brand__mark"></span>
    <span class="brand__name">MORVANE TALLY</span>
  </div>

  <div class="contact">
    Derek Wallis - Chief Operations Officer<br>
    P : 02 7153 2819<br>
    M: 0418 395 207<br>
    derek@morvanetally.com
  </div>
</section>
<div class="side-label side-label--front">Front</div>

<section class="card card--back">
  <svg class="card__stripes" viewBox="0 0 1027 625" preserveAspectRatio="none" aria-hidden="true">
    <polygon class="stripe--blue" points="0,291 277,180 1027,185 1027,188 281,197 0,295"/>
    <polygon class="stripe--grey" points="0,447 747,433 1027,337 1027,341 752,451 0,450"/>
  </svg>
  <p class="service service--exchange">Cryptocurrency Exchange Services</p>
  <p class="service service--mining">Cryptocurrency Mining Operations</p>
  <p class="service service--fund">Cryptocurrency Investment Fund Offering</p>
</section>
<div class="side-label side-label--back">Back</div>

</body>
</html>
```